webdesign for a spectacles/glasses designer

Hello,

Someone in my village designs his own spectacles/eyeglasses.

For this I need a design that looks better than my poor design skills ;o)

The site is based around collections, subcollections and the actual items.

So we need a design that lists these in a nice way, worst case on seperate pages.

Here you can find the working material...

https://www.filevault-example.com/s/q8rtk2mzp4vn71c/ArtHive.zip

keep an eye on the product_tree file.

first level is the collection name
2nd is the model group
3rd is the model (on most of them it's just a different color of the same base model)

I added a seperate contact info file (line is too slow to reupload 60Mb again :( )

https://dl.filevault-example.com/u/31946082/Marten/contact.zip

I think I forgot to mention that it will be a shop like site to present his products,
altho I will add a cart system there won't be a payment system linked to it as
people who place orders will get contacted with payment instructions.
Updates

In the zipfile /Logo/logo_mistral_font.psd is the main logo
(you need to change character spacing to 1 to get rid of the spacing gaps)

the other one is only a collection logo

Target Market(s)

Plain customers and his resellers.

Industry/Entity Type

Shop

Requirements
Must have
• - a design that suits responsive behaviour (via the 960 grid)
- a menu is always handy (home, about, collections, contact)
- highlighted area/slider to highlight his sunglasses over glasses thingy
- featured products (newly added or promotional stuff)

there is a lot of pretty pictures to be supplied so do what you think is best

Nice to have
• a roll over zoom with selectable thumbnails or a plain gallery with full picture display at the product page.

maybe a drop down menu for the collection part (I will supply a screenshot of the backend structure)

```html
<!DOCTYPE html>
<html lang="en">
<head>
<meta charset="utf-8">
<title>Lumen Frames — Eyewear</title>
<link rel="stylesheet" href="https://fonts.googleapis.com/css2?family=Open+Sans:ital,wght@0,300;0,400;0,600;0,700;1,400&family=Cormorant+Garamond:ital,wght@1,500&display=swap">
<style>
:root{
  --bar:#2f3131;
  --ink:#4a4d4a;
  --heading:#4b5147;
  --white:#ffffff;
  --rule:#8a8a8a;
  --nav-active:#8e918e;
  --green:#2cbf3a;
  --cyan:#19b8e6;
  --btn-top:#ffffff;
  --btn-bottom:#dcdcdc;
  --btn-text:#555;
  --addr:#b7e6a8;
}
*{box-sizing:border-box;margin:0;padding:0}
html,body{width:944px;height:1200px;overflow:hidden;background:var(--white)}
body{position:relative;font-family:"Open Sans",Tahoma,sans-serif;color:var(--ink)}
.abs{position:absolute}

/* header */
.site-header{left:0;top:0;width:944px;height:66px;background:var(--bar)}
.brand{left:18px;top:18px;display:flex;align-items:center;gap:8px;color:var(--white);font-size:20px;font-weight:600;letter-spacing:.5px}
.brand-dot{width:14px;height:14px;border-radius:50%;background:var(--cyan)}
.main-nav{left:0;top:19px;height:35px}
.main-nav a{position:absolute;top:0;height:35px;line-height:35px;padding:0 9px;color:var(--white);font-size:16.5px;text-decoration:none;text-shadow:0 1px 2px rgba(0,0,0,.7);white-space:nowrap}
.main-nav a.is-active{background:var(--nav-active)}

/* hero */
.hero{left:0;top:66px;width:944px;height:308px;background:
  linear-gradient(160deg,rgba(255,255,255,.65) 0%,rgba(255,255,255,0) 35%),
  linear-gradient(100deg,#9fdc8a 0%,#5cc95a 30%,#c9ecd7 55%,#7fd9cf 75%,#1fc0c7 100%)}
.hero-band{left:0;top:364px;width:944px;height:10px;background:linear-gradient(90deg,#b6e4a6,#8fdcdf)}
.hero-title{left:33px;top:60px;width:440px;color:var(--white);font-size:32px;font-weight:400;line-height:42px;text-shadow:0 1px 3px rgba(0,0,0,.45)}
.hero-photo{left:455px;top:105px;width:375px;height:172px;border-radius:40px;background:radial-gradient(ellipse at center,rgba(40,70,200,.55),rgba(40,70,200,0) 70%)}
.btn{display:block;text-align:center;border-radius:7px;background:linear-gradient(var(--btn-top),var(--btn-bottom));box-shadow:0 2px 3px rgba(0,0,0,.35);color:var(--btn-text);font-size:13.5px;text-transform:uppercase;border:1px solid #bdbdbd}
.hero .btn{top:172px;width:164px;height:41px;line-height:39px}

/* products */
.section-title{color:var(--heading);font-weight:700;font-size:22px}
.rule{height:0;border-top:1px dotted var(--rule)}
.product{top:437px;width:281px}
.product-photo{width:281px;height:140px;background:linear-gradient(#f4f4f6,#e2e2e8)}
.product-photo.white{background:#ffffff;border:1px solid #f2f2f2}
.product h3{margin-top:13px;font-size:17.5px;font-weight:600;color:var(--heading);white-space:nowrap}
.product p{margin-top:10px;font-size:11.5px;line-height:17px}

/* feature */
.feature-title{left:33px;top:727px;font-size:24px;font-weight:700;color:var(--heading)}
.feature-text{left:33px;top:760px;width:510px;font-size:11.5px;line-height:17px}
.feature-photo{left:33px;top:878px;width:355px;height:80px;border-radius:20px;background:linear-gradient(90deg,#8c4a1e,#c98a4a,#8c4a1e)}
.feature .btn{left:411px;top:897px;width:108px;height:41px;line-height:39px}
.divider{left:558px;top:722px;width:2px;height:265px;background:linear-gradient(rgba(0,0,0,0),rgba(0,0,0,.18) 40%,rgba(0,0,0,0))}

/* blog */
.blog-title{left:575px;top:730px;font-size:17.5px;font-weight:600;color:var(--heading)}
.post{left:575px;width:340px;display:flex;gap:13px}
.post-thumb{flex:none;width:62px;height:62px;border:2px solid #d6d6d6}
.post-thumb.pink{background:linear-gradient(135deg,#f7a8d8,#e65cb5)}
.post-thumb.yellow{background:linear-gradient(135deg,#ffe65a,#f2c21a)}
.post h4{font-size:13.5px;font-weight:400;color:#333;margin-top:-4px}
.post p{font-size:11.5px;line-height:17px;margin-top:2px}

/* footer */
.site-footer{left:0;top:1011px;width:944px;height:189px;background:
  linear-gradient(155deg,rgba(255,255,255,0) 30%,rgba(255,255,255,.25) 45%,rgba(255,255,255,0) 60%),
  linear-gradient(95deg,#13a81f 0%,#22b84a 35%,#0fb59a 65%,#06b4ef 100%)}
.footer-col{top:34px;width:210px;color:var(--white)}
.footer-col h5{font-size:22px;font-weight:300;text-shadow:0 1px 2px rgba(0,0,0,.3)}
.footer-col address,.footer-col .lines{margin-top:12px;font-family:"Cormorant Garamond",Georgia,serif;font-style:italic;font-size:14.5px;line-height:16px;color:var(--addr)}
.footer-sep{top:29px;width:1px;height:88px;background:rgba(255,255,255,.45)}
.email-field{position:absolute;left:0;top:37px;width:148px;height:34px;border:2px solid #8ed38a;background:#3fc13b;padding-left:7px;font-family:"Cormorant Garamond",Georgia,serif;font-style:italic;font-size:14px;line-height:30px;color:#a6e39c}
.go-btn{position:absolute;left:152px;top:37px;width:36px;height:36px;line-height:34px;font-size:12px;border-radius:8px}
.social{display:flex;gap:17px;margin-top:13px}
.social span{width:30px;height:30px;border-radius:5px;background:rgba(255,255,255,.85)}
.footer-rule{left:0;top:141px;width:944px;height:1px;background:rgba(255,255,255,.55)}
.copyright{left:24px;top:157px;font-size:12.5px;color:var(--white);text-shadow:0 1px 2px rgba(0,0,0,.5)}
</style>
</head>
<body>

<header class="site-header abs">
  <div class="brand abs"><span class="brand-dot"></span>Lumen Frames</div>
  <nav class="main-nav abs">
    <a class="is-active" href="#" style="left:463px">Home</a>
    <a href="#" style="left:534px">Products</a>
    <a href="#" style="left:625px">Blog</a>
    <a href="#" style="left:687px">About</a>
    <a href="#" style="left:759px">Contact</a>
  </nav>
</header>

<section class="hero abs">
  <h1 class="hero-title abs" style="top:-6px">Lorem ipsum dolor sit amet, consecteteur adipiscing elit Aliquam ac duia praesent.</h1>
  <div class="hero-photo abs" style="top:39px" role="img" aria-label="Blue rectangular eyeglasses floating above the green and turquoise backdrop"></div>
  <a class="btn abs" href="#" style="left:33px">View our glasses</a>
  <a class="btn abs" href="#" style="left:248px">View other stuff</a>
</section>
<div class="hero-band abs"></div>

<h2 class="section-title abs" style="left:33px;top:386px">Our Glasses</h2>
<div class="rule abs" style="left:33px;top:418px;width:879px"></div>

<article class="product abs" style="left:33px">
  <div class="product-photo white" role="img" aria-label="Rimless glasses with patterned temples"></div>
  <h3>Maecenas eu felis non elit eges</h3>
  <p>Suspendisse arcu nunc, dapibus viverra, eleifend at, posuere vitae, orci. Aliquam tempus dui sit amet odio. Morbi viverra leo eu purus. Phasellus nec ligula. Duis at erat. Donec sodales. More...</p>
</article>
<article class="product abs" style="left:332px">
  <div class="product-photo" role="img" aria-label="Black full-rim glasses on a light grey surface"></div>
  <h3>Maecenas eu felis non elit eges</h3>
  <p>Suspendisse arcu nunc, dapibus viverra, eleifend at, posuere vitae, orci. Aliquam tempus dui sit amet odio. Morbi viverra leo eu purus. Phasellus nec ligula. Duis at erat. Donec sodales. More...</p>
</article>
<article class="product abs" style="left:632px">
  <div class="product-photo" role="img" aria-label="Half-rim silver and black glasses on a light grey surface"></div>
  <h3>Maecenas eu felis non elit eges</h3>
  <p>Suspendisse arcu nunc, dapibus viverra, eleifend at, posuere vitae, orci. Aliquam tempus dui sit amet odio. Morbi viverra leo eu purus. Phasellus nec ligula. Duis at erat. Donec sodales. More...</p>
</article>

<div class="rule abs" style="left:33px;top:709px;width:879px;border-top-style:solid;border-color:#bbb"></div>

<section class="feature">
  <h2 class="feature-title abs">Curabitur bibendum magna. Donec velit.</h2>
  <p class="feature-text abs">Sed euismod erat eu sem. Nam eu erat in mi semper tempor. Donec congue, augue in feugiat congue, magna pede tristique ligula, vitae ultrices erat justo ut purus. Mauris ante. Aenean est velit, scelerisque a, auctor ut, accumsan ut, augue. Proin in velit. Aliquam ac dui. Praesent congue leo eu nunc. Curabitur imperdiet, nulla sed feugiat pretium, elit ante blandit mi, non tempor est ligula id ipsum. Morbi metus. Pellentesque tellus. Proin sed velit. Suspendisse fringilla ornare elit. Pellentesque ac augue. Curabitur vestibulum lorem at velit.</p>
  <div class="feature-photo abs" role="img" aria-label="Tortoiseshell brown rectangular glasses"></div>
  <a class="btn abs" href="#">More info</a>
</section>
<div class="divider abs"></div>

<aside>
  <h2 class="blog-title abs">Latest from the blog</h2>
  <article class="post abs" style="top:773px">
    <div class="post-thumb pink" role="img" aria-label="Pink abstract blog thumbnail"></div>
    <div>
      <h4>Sed euismod erat eu sem nam eu</h4>
      <p>Quisque venenatis, ipsum nec tincidunt ultrices, sem metus mattis erat, molestie scelerisque dolor augue ut orci. Maecenas vehicula dignissim leo. Continue reading "Sed uismod erat..."</p>
    </div>
  </article>
  <article class="post abs" style="top:881px">
    <div class="post-thumb yellow" role="img" aria-label="Yellow abstract blog thumbnail"></div>
    <div>
      <h4>Sed euismod erat eu sem nam eu</h4>
      <p>Quisque venenatis, ipsum nec tincidunt ultrices, sem metus mattis erat, molestie scelerisque dolor augue ut orci. Maecenas vehicula dignissim leo. Continue reading "Sed uismod erat..."</p>
    </div>
  </article>
</aside>

<footer class="site-footer abs">
  <div class="footer-col abs" style="left:24px">
    <h5>Mailing List</h5>
    <div class="email-field">me@myemail.com</div>
    <a class="btn go-btn" href="#">Go</a>
  </div>
  <div class="footer-sep abs" style="left:230px"></div>
  <div class="footer-col abs" style="left:250px">
    <h5>Address</h5>
    <address>480 Linden Lane,<br>Fernbrook, 20417 Eastvale</address>
  </div>
  <div class="footer-sep abs" style="left:457px"></div>
  <div class="footer-col abs" style="left:476px;width:220px">
    <h5>Contact Us</h5>
    <p class="lines">Phone: (555) 019-4472<br>hello@brightmoorstudio.example</p>
  </div>
  <div class="footer-sep abs" style="left:683px"></div>
  <div class="footer-col abs" style="left:703px">
    <h5>Connect With Us</h5>
    <div class="social">
      <span role="img" aria-label="Social network link"></span>
      <span role="img" aria-label="Social network link"></span>
      <span role="img" aria-label="Photo sharing link"></span>
      <span role="img" aria-label="News feed link"></span>
    </div>
  </div>
  <div class="footer-rule abs"></div>
  <p class="copyright abs">©2010 Brightmoor Studio LLC. All rights reserved.</p>
</footer>

</body>
</html>
```